Bref créative
leap fern boots homepage
selling leap fern boots and glide to live book
Apparel
www.leapfernboots-demo.com (not live)
Leap fern boots...leap home to earth. Runners are running barefoot more than ever and leapfern boots is the minimal shoe that will help the runner transition back to nature.. Running Barefoot!
About us: Leap Fern Boots are created to get the runner back to nature. These shoes are designed to transition the runner from running shoes to leap fern boots and eventually running barefoot. Leap Fern Boots are lightweight and developed to handle the terrain and pavement as if you weren’t wearing any shoes at all. The Barefoot running alternative!
Natural, Eco Friendly, Scientific,
approved logo is attached
http://www.quilvantor.com/contests/leap-fern-boots/users/TOBYstudio
I own the mov
http://www.pelmarclips.com/stock-video-5820913-neon-sprint-figure-cycle.php
Black
White/ beige
left side
http://www.vekzo.org/
http://www.lum.org/
http://www.pelmarclips.com/
I have 105 credits at Pel mar clips.com feel free to browse and use pictures in front page. Purpose of site is to sell a book live to glide and leapfernboots. I like banners, for example the banner shoes a pair of shoes and moves on to the next banner showing the book with buy now buttons. mov file available as well. I will have a jpeg of shoes later...for now just find a pair and use that and we will switch it out

```html
<!DOCTYPE html>
<html lang="en">
<head>
<meta charset="utf-8">
<title>Leap Fern Boots — Home</title>
<link rel="stylesheet" href="https://fonts.googleapis.com/css2?family=Arimo:wght@400;700&display=swap">
<style>
  :root {
    --leaf: #8cc63f;
    --leaf-dark: #5d9a1e;
    --ink: #111111;
    --paper: #ffffff;
    --sky-top: #6f8fb0;
    --sky-low: #c9d6e2;
    --grass: #4f8a2a;
    --book-top: #f2a23a;
    --book-low: #6f8fbf;
  }
  * { margin: 0; padding: 0; box-sizing: border-box; }
  html, body {
    width: 1200px;
    height: 901px;
    overflow: hidden;
    background: var(--paper);
    font-family: "Arimo", Arial, sans-serif;
    color: var(--ink);
  }
  .page {
    position: relative;
    width: 1200px;
    height: 901px;
  }
  .brand {
    position: absolute;
    left: 172px;
    top: 34px;
    display: flex;
    align-items: center;
    gap: 18px;
    color: var(--leaf-dark);
    font-size: 62px;
    font-weight: 700;
    letter-spacing: 1px;
  }
  .brand-mark {
    width: 30px;
    height: 30px;
    border-radius: 50%;
    background: var(--leaf-dark);
  }
  .main-nav {
    position: absolute;
    left: 131px;
    top: 151px;
    width: 300px;
    height: 341px;
    background: var(--leaf);
    display: flex;
    flex-direction: column;
    justify-content: center;
    align-items: center;
    gap: 0;
  }
  .main-nav a {
    color: var(--paper);
    text-decoration: none;
    font-size: 36px;
    line-height: 54px;
  }
  .hero-photo {
    position: absolute;
    left: 458px;
    top: 151px;
    width: 611px;
    height: 341px;
    background: linear-gradient(180deg, var(--sky-top) 0%, var(--sky-low) 65%, var(--grass) 80%, var(--grass) 100%);
  }
  .book-cover {
    position: absolute;
    left: 209px;
    top: 531px;
    width: 124px;
    height: 189px;
    background: linear-gradient(180deg, var(--book-top) 0%, var(--book-top) 30%, var(--book-low) 100%);
  }
  .intro {
    position: absolute;
    left: 462px;
    top: 524px;
    width: 600px;
    font-size: 19px;
    line-height: 26px;
    text-align: center;
  }
  .site-footer {
    position: absolute;
    left: 0;
    top: 836px;
    width: 1200px;
    text-align: center;
    font-size: 16px;
    line-height: 27px;
  }
  .site-footer a {
    color: var(--ink);
    text-decoration: none;
  }
</style>
</head>
<body>
<div class="page">
  <header class="brand">
    <span>Leap Fern Boots</span>
    <span class="brand-mark" aria-hidden="true"></span>
  </header>

  <nav class="main-nav">
    <a href="#">Home</a>
    <a href="#">About Us</a>
    <a href="#">Products</a>
    <a href="#">Sponsors</a>
    <a href="#">Feedback</a>
    <a href="#">Contact Us</a>
  </nav>

  <div class="hero-photo" role="img" aria-label="Photo of a runner sprinting barefoot across a grassy field under a cloudy sky"></div>

  <div class="book-cover" role="img" aria-label="Cover of the book Live to Glide with a runner on a hilltop"></div>

  <p class="intro">Leap Fern Boots are created to get the runner back to nature. These shoes are designed to transition the runner from running shoes to leap fern boots and eventually running barefoot. Leap Fern Boots are light-weight and developed to handle the terrain and pavement as if you weren't wearing any shoes at all. The Barefoot running alternative!</p>

  <footer class="site-footer">
    <div><a href="#">Home</a> | <a href="#">About Us</a> | <a href="#">Products</a> | <a href="#">Sponsors</a> | <a href="#">Feedback</a> | <a href="#">Contact Us</a></div>
    <div>Copyright© 2010 Meadow Stride Collective</div>
  </footer>
</div>
</body>
</html>
```